Brimlow Oakville Cabernet Sauvignon-Wine label design

We need a package design for an up market wine brand named, Brimlow. It will be a Cabernet Sauvignon from the Oakville AVA of Napa Valley. We are looking for a stylish modern label that will stand out on a retail shelf. We want the label to be attention grabbing and stylish while presenting an up market luxury brand.
Updates

Sick

Requirements
Must have
• Must have the words(in order of importance)
-Brimlow
-Cabernet Sauvignon
-Oakville
-Napa Valley
-2018

Must be designed for a traditional "Bordeaux" style bottle (Bottle specs in uploaded files)
Should not have
• Any images of grapes, vineyards, wine glasses or bottles

```html
<!DOCTYPE html>
<html lang="en">
<head>
<meta charset="utf-8">
<title>Brimlow Cabernet Sauvignon – Label</title>
<link rel="stylesheet" href="https://fonts.googleapis.com/css2?family=Josefin+Sans:wght@300&family=Lato:wght@400&display=swap">
<style>
  :root {
    --paper: #f8f8ee;
    --label-white: #f1f1ec;
    --ink: #3a3a3a;
    --rose: #c4587e;
    --magenta: #a8386a;
    --coral: #e07a6a;
    --lilac: #a9a8cf;
    --violet: #6c67a8;
    --plum: #5a3c78;
  }
  * { box-sizing: border-box; margin: 0; padding: 0; }
  html, body { width: 1200px; height: 900px; overflow: hidden; }
  body {
    background: var(--paper);
    display: flex;
    align-items: center;
    justify-content: center;
  }
  .label {
    width: 620px;
    height: 780px;
    display: flex;
    flex-direction: column;
    box-shadow: 0 10px 30px rgba(0,0,0,0.12);
  }
  .label__art {
    flex: 1;
    display: block;
    width: 100%;
  }
  .label__band {
    height: 170px;
    background: var(--label-white);
    display: flex;
    align-items: center;
    gap: 26px;
    padding: 0 44px;
  }
  .brand-name {
    font-family: "Josefin Sans", sans-serif;
    font-weight: 300;
    font-size: 64px;
    letter-spacing: 4px;
    color: var(--ink);
    line-height: 1;
    padding-top: 8px;
  }
  .wine-details {
    font-family: "Lato", sans-serif;
    color: var(--ink);
  }
  .wine-details__varietal {
    font-size: 17px;
    letter-spacing: 0.5px;
    padding-bottom: 5px;
    border-bottom: 1.5px solid var(--ink);
    text-transform: uppercase;
  }
  .wine-details__origin {
    font-size: 13px;
    padding-top: 5px;
    letter-spacing: 0.5px;
  }
</style>
</head>
<body>
  <main class="label">
    <svg class="label__art" viewBox="0 0 620 610" preserveAspectRatio="none"
         role="img" aria-label="Abstract artwork of overlapping translucent waves in rose, coral and violet">
      <defs>
        <linearGradient id="artwash" x1="0" y1="0" x2="0" y2="1">
          <stop offset="0" stop-color="#c4587e"/>
          <stop offset="0.3" stop-color="#a8386a"/>
          <stop offset="0.48" stop-color="#e07a6a"/>
          <stop offset="0.62" stop-color="#a9a8cf"/>
          <stop offset="0.82" stop-color="#6c67a8"/>
          <stop offset="1" stop-color="#5a3c78"/>
        </linearGradient>
      </defs>
      <rect width="620" height="610" fill="url(#artwash)"/>
    </svg>
    <section class="label__band">
      <h1 class="brand-name">BRIMLOW</h1>
      <div class="wine-details">
        <p class="wine-details__varietal">Cabernet Sauvignon</p>
        <p class="wine-details__origin">Oakville - Napa Valley - 2018</p>
      </div>
    </section>
  </main>
</body>
</html>
```